Supplement Rebranding Bottle Design

READ WORD DOCUMENT ATTACHED.
We want to rebrand our current health supplements (see below). We do want it to be modern, vibrant and appealing. Very upscale and elegant as it targets primarily women.
Bottle size: see pictures for bottle size, along with sample bottles that we like; we’re open to any bottle similar to the ones attached.
Current bottles: So ideally, we’d keep the core color on each bottle with a new branding/bottle design. But we're open to your suggestion.

Target Market(s)

mostly women but shouldn't be overly feminine

Requirements
Must have
• see bottle sizes attached

```html
<!DOCTYPE html>
<html lang="en">
<head>
<meta charset="utf-8">
<title>Bloom Supplement Labels</title>
<link href="https://fonts.googleapis.com/css2?family=Montserrat:wght@600;700;800&display=swap" rel="stylesheet">
<style>
  :root {
    --bg: #e7e7e7;
    --ink: #1f1f1f;
    --white: #ffffff;
    --liver: #6b2545;      --liver-accent: #c0508c;
    --glucose: #41346a;    --glucose-accent: #6580c4;
    --hormone: #234d47;    --hormone-accent: #82c9a9;
    --tummy: #c82632;      --tummy-accent: #f06e7c;
  }
  * { box-sizing: border-box; margin: 0; padding: 0; }
  html, body { width: 1200px; height: 1000px; overflow: hidden; }
  body { background: var(--bg); font-family: "Montserrat", Arial, sans-serif; position: relative; }

  .label {
    position: absolute; width: 248px; height: 268px; overflow: hidden;
    background: linear-gradient(90deg, #eeeeee 0%, #ffffff 45%, #ffffff 60%, #e6e6e6 100%);
    box-shadow: 0 2px 4px rgba(0,0,0,.18);
    color: var(--ink); text-align: center; font-weight: 700;
  }
  .liver   { --c: var(--liver);   --a: var(--liver-accent);   --r: var(--liver-accent); }
  .glucose { --c: var(--glucose); --a: var(--glucose-accent); --r: var(--glucose); }
  .hormone { --c: var(--hormone); --a: var(--hormone-accent); --r: var(--hormone); }
  .tummy   { --c: var(--tummy);   --a: var(--tummy-accent);   --r: var(--tummy); }

  .row-top .label { top: 196px; }
  .row-bottom .label { top: 500px; }
  .col-1 { left: 72px; } .col-2 { left: 340px; } .col-3 { left: 612px; } .col-4 { left: 882px; }

  .name { position: absolute; left: 0; right: 0; font-size: 20px; font-weight: 700; letter-spacing: .5px; line-height: 1; }
  .name .pre { display: block; font-size: 13px; color: var(--a); margin-bottom: 3px; letter-spacing: .5px; }

  .claim { position: absolute; left: 0; right: 0; font-size: 14px; line-height: 17px; letter-spacing: .3px; }
  .claim.large { font-size: 16px; line-height: 20px; }
  .footer {
    position: absolute; left: 0; right: 0; bottom: 0; height: 23px; padding: 0 10px;
    display: flex; justify-content: space-between; align-items: center; font-size: 9px; letter-spacing: .2px;
  }
  .qty-key { color: var(--a); margin-right: 3px; }

  /* top series */
  .row-top .cap { position: absolute; top: 0; left: 0; width: 248px; height: 112px; }
  .row-top .cap path { fill: var(--c); }
  .row-top .name { top: 46px; color: var(--white); }
  .row-top .name.has-pre { top: 29px; }
  .row-top .name.raised { top: 39px; }
  .row-top .claim { top: 142px; }
  .row-top .claim.large { top: 136px; }
  .row-top .rule { position: absolute; top: 188px; left: 108px; width: 32px; height: 2px; background: var(--r); }
  .row-top .type { position: absolute; top: 206px; left: 0; right: 0; font-size: 13px; letter-spacing: .3px; }
  .row-top .footer { background: var(--c); color: var(--white); }

  /* bottom series */
  .row-bottom .strip { position: absolute; top: 0; left: 0; right: 0; height: 8px; background: var(--a); }
  .row-bottom .name { top: 54px; color: var(--c); }
  .row-bottom .name.has-pre { top: 37px; }
  .row-bottom .name.lowered { top: 56px; }
  .row-bottom .band { position: absolute; top: 117px; left: 0; right: 0; height: 96px; background: var(--c); }
  .row-bottom .claim { top: 145px; color: var(--white); }
  .row-bottom .claim.large { top: 140px; }
  .row-bottom .pill {
    position: absolute; top: 199px; left: 19px; width: 210px; height: 27px; border-radius: 14px;
    background: var(--a); color: var(--white); font-size: 13px; line-height: 27px; letter-spacing: .3px;
  }
  .row-bottom .footer { bottom: 2px; }
</style>
</head>
<body>

<section class="row-top">
  <article class="label liver col-1">
    <svg class="cap" viewBox="0 0 248 112" preserveAspectRatio="none" aria-hidden="true"><path d="M0 0H248V90Q124 126 0 90Z"/></svg>
    <h2 class="name">LIVER BLOOM</h2>
    <p class="claim">REJUVENATING CLEANSE<br>&amp; DETOX FORMULA*</p>
    <div class="rule"></div>
    <p class="type">DIETARY SUPPLEMENT</p>
    <div class="footer"><span><span class="qty-key">QTY</span>120</span><span>VEGETABLE CAPSULES</span></div>
  </article>
  <article class="label glucose col-2">
    <svg class="cap" viewBox="0 0 248 112" preserveAspectRatio="none" aria-hidden="true"><path d="M0 0H248V90Q124 126 0 90Z"/></svg>
    <h2 class="name has-pre"><span class="pre">BLOOD</span>SUGAR BLOOM</h2>
    <p class="claim">SUPPORTS HEALTHY<br>BLOOD GLUCOSE LEVELS*</p>
    <div class="rule"></div>
    <p class="type">DIETARY SUPPLEMENT</p>
    <div class="footer"><span><span class="qty-key">QTY</span>60</span><span>VEGETABLE CAPSULES</span></div>
  </article>
  <article class="label hormone col-3">
    <svg class="cap" viewBox="0 0 248 112" preserveAspectRatio="none" aria-hidden="true"><path d="M0 0H248V90Q124 126 0 90Z"/></svg>
    <h2 class="name raised">HORMONE BLOOM</h2>
    <p class="claim">SUPPORTS HEALTHY<br>HORMONE LEVELS*</p>
    <div class="rule"></div>
    <p class="type">DIETARY SUPPLEMENT</p>
    <div class="footer"><span><span class="qty-key">QTY</span>60</span><span>VEGETABLE CAPSULES</span></div>
  </article>
  <article class="label tummy col-4">
    <svg class="cap" viewBox="0 0 248 112" preserveAspectRatio="none" aria-hidden="true"><path d="M0 0H248V90Q124 126 0 90Z"/></svg>
    <h2 class="name raised">TUMMY BLOOM</h2>
    <p class="claim large">OXYGENATING<br>COLON CLEANSE*</p>
    <div class="rule"></div>
    <p class="type">DIETARY SUPPLEMENT</p>
    <div class="footer"><span><span class="qty-key">QTY</span>90</span><span>VEGETABLE CAPSULES</span></div>
  </article>
</section>

<section class="row-bottom">
  <article class="label liver col-1">
    <div class="strip"></div>
    <h2 class="name">LIVER BLOOM</h2>
    <div class="band"></div>
    <p class="claim">REJUVENATING CLEANSE<br>&amp; DETOX FORMULA*</p>
    <p class="pill">DIETARY SUPPLEMENT</p>
    <div class="footer"><span><span class="qty-key">QTY</span>120</span><span>VEGETABLE CAPSULES</span></div>
  </article>
  <article class="label glucose col-2">
    <div class="strip"></div>
    <h2 class="name has-pre"><span class="pre">BLOOD</span>SUGAR BLOOM</h2>
    <div class="band"></div>
    <p class="claim">SUPPORTS HEALTHY<br>BLOOD GLUCOSE LEVELS*</p>
    <p class="pill">DIETARY SUPPLEMENT</p>
    <div class="footer"><span><span class="qty-key">QTY</span>60</span><span>VEGETABLE CAPSULES</span></div>
  </article>
  <article class="label hormone col-3">
    <div class="strip"></div>
    <h2 class="name lowered">HORMONE BLOOM</h2>
    <div class="band"></div>
    <p class="claim">SUPPORTS HEALTHY<br>HORMONE LEVELS*</p>
    <p class="pill">DIETARY SUPPLEMENT</p>
    <div class="footer"><span><span class="qty-key">QTY</span>60</span><span>VEGETABLE CAPSULES</span></div>
  </article>
  <article class="label tummy col-4">
    <div class="strip"></div>
    <h2 class="name">TUMMY BLOOM</h2>
    <div class="band"></div>
    <p class="claim large">OXYGENATING<br>COLON CLEANSE*</p>
    <p class="pill">DIETARY SUPPLEMENT</p>
    <div class="footer"><span><span class="qty-key">QTY</span>90</span><span>VEGETABLE CAPSULES</span></div>
  </article>
</section>

</body>
</html>
```